Online retailer needs a Quirky yet professionally designed double sided business car

We mainly sell kitchen and home accessories but pretty much anything new and in demand. Have a look at our site and then come up with designs.
Design to be really catching and want people to visit the website.
Final details such as number, director name and email address will be given to the designer of the winning business card.

Www.zapfinda.com

Ideas out of the norm also welcome!!

```html
<!DOCTYPE html>
<html lang="en">
<head>
<meta charset="utf-8">
<title>Zapfinda business card</title>
<link rel="stylesheet" href="https://fonts.googleapis.com/css2?family=Open+Sans:wght@400;600;700&display=swap">
<style>
  :root {
    --stage: #1c1c1c;
    --paper: #ffffff;
    --brand-orange: #f0801f;
    --ink: #151515;
    --photo-light: #f4f4f4;
    --photo-mid: #c9c9c9;
    --shadow: rgba(0, 0, 0, 0.18);
  }
  * { box-sizing: border-box; margin: 0; padding: 0; }
  html, body {
    width: 1200px;
    height: 1000px;
    overflow: hidden;
    background: var(--stage);
    font-family: "Open Sans", Arial, sans-serif;
  }
  .canvas {
    position: relative;
    width: 1200px;
    height: 1000px;
  }
  .card {
    position: absolute;
    left: 240px;
    width: 720px;
    height: 430px;
    background: var(--paper);
    overflow: hidden;
  }
  .card--front { top: 50px; }
  .card--back {
    top: 520px;
    border: 18px solid var(--brand-orange);
  }

  /* brand name */
  .brand {
    position: absolute;
    display: flex;
    align-items: center;
    gap: 12px;
  }
  .card--front .brand { left: 46px; top: 62px; }
  .card--back .brand { left: 50%; top: 50%; transform: translate(-50%, -50%); }
  .brand__dot {
    width: 30px; height: 30px;
    border-radius: 50%;
    background: var(--brand-orange);
  }
  .brand__name {
    font-family: "Open Sans", Arial, sans-serif;
    font-weight: 700;
    font-size: 48px;
    line-height: 1;
    color: var(--ink);
  }

  /* orange band */
  .band { position: absolute; left: 0; top: 0; }

  .products {
    position: absolute;
    left: 38px;
    top: 215px;
    display: flex;
    gap: 34px;
  }
  .product {
    width: 116px; height: 116px;
    border-radius: 50%;
    background: var(--paper);
    display: flex; align-items: center; justify-content: center;
    box-shadow: 0 10px 10px -6px var(--shadow);
  }
  .product__photo {
    width: 92px; height: 92px;
    border-radius: 50%;
    background: radial-gradient(circle at 50% 45%, var(--photo-light), var(--photo-mid));
  }

  .person {
    position: absolute;
    left: 530px;
    top: 178px;
    color: var(--paper);
  }
  .person__name { font-weight: 700; font-size: 17px; }
  .person__role { font-size: 14px; }

  .contacts {
    position: absolute;
    left: 28px;
    right: 20px;
    bottom: 22px;
    display: flex;
    justify-content: space-between;
    list-style: none;
    color: var(--paper);
    font-size: 13px;
  }
  .contact { display: flex; align-items: center; gap: 7px; }
  .contact svg { width: 13px; height: 13px; fill: var(--paper); }
</style>
</head>
<body>
<main class="canvas">

  <section class="card card--front">
    <svg class="band" width="720" height="430" viewBox="0 0 720 430" aria-hidden="true">
      <path fill="var(--brand-orange)"
        d="M0 300 C0 240 40 190 110 190 L470 190 C490 190 500 178 505 165
           C515 140 535 128 565 128 L650 128 C690 128 720 158 720 198 L720 430 L0 430 Z"/>
    </svg>

    <div class="brand">
      <span class="brand__dot"></span>
      <span class="brand__name">Zapfinda</span>
    </div>

    <div class="person">
      <p class="person__name">Your Name here</p>
      <p class="person__role">Designation</p>
    </div>

    <div class="products">
      <div class="product"><div class="product__photo" role="img" aria-label="Photo of a folding kitchen trivet"></div></div>
      <div class="product"><div class="product__photo" role="img" aria-label="Photo of a glass infuser water bottle"></div></div>
      <div class="product"><div class="product__photo" role="img" aria-label="Photo of a steel wine bottle cooler"></div></div>
      <div class="product"><div class="product__photo" role="img" aria-label="Photo of a wine aerator on a glass"></div></div>
    </div>

    <ul class="contacts">
      <li class="contact">
        <svg viewBox="0 0 12 12"><path d="M6 0a4 4 0 0 0-4 4c0 3 4 8 4 8s4-5 4-8a4 4 0 0 0-4-4zm0 5.5a1.5 1.5 0 1 1 0-3 1.5 1.5 0 0 1 0 3z"/></svg>
        Address here Street,city, country
      </li>
      <li class="contact">
        <svg viewBox="0 0 12 12"><path d="M3 0h6v12H3zM4 1v9h4V1zm1.5 9.6h1v.8h-1z"/></svg>
        +91 8000 314 159
      </li>
      <li class="contact">
        <svg viewBox="0 0 12 12"><path d="M0 2h12v8H0zm1 1v.4l5 3.4 5-3.4V3z"/></svg>
        email@zapmail.com
      </li>
      <li class="contact">
        <svg viewBox="0 0 12 12"><path d="M6 0a6 6 0 1 0 0 12A6 6 0 0 0 6 0zm0 1.2c.7.8 1.2 2.3 1.3 4.2H4.7C4.8 3.5 5.3 2 6 1.2zM1.2 6.6h2.5c.1 1.7.5 3.1 1.1 4.1A4.8 4.8 0 0 1 1.2 6.6zm0-1.2a4.8 4.8 0 0 1 3.6-4.1c-.6 1-1 2.4-1.1 4.1zm3.5 1.2h2.6C7.2 8.5 6.7 10 6 10.8c-.7-.8-1.2-2.3-1.3-4.2zm3.6 4.1c.6-1 1-2.4 1.1-4.1h2.5a4.8 4.8 0 0 1-3.6 4.1zm1.1-5.3c-.1-1.7-.5-3.1-1.1-4.1a4.8 4.8 0 0 1 3.6 4.1z"/></svg>
        yourwebsite.com
      </li>
    </ul>
  </section>

  <section class="card card--back">
    <div class="brand">
      <span class="brand__dot"></span>
      <span class="brand__name">Zapfinda</span>
    </div>
  </section>

</main>
</body>
</html>
```